swimming pool chlorine

its label for new items we have its coming with different package 5 & 10 & 45 kg drums its specialized for making the swimming pool clean of all dirts we have our logo which I will attach its " Valmo" but we need the label to show the clear of pool and the logo in middle top and down write " TORVA 60 with nice design. under this name of metreal "TRICHOROISOCYANURIC ACID" and we want to add some advantage of the product which is" Strong bleaching and disinfection effects, Long-term effects, Killing Bacteria and Algae, Quality Guarantee.

```html
<!DOCTYPE html>
<html lang="en">
<head>
<meta charset="utf-8">
<title>Valmo TORVA 60 – Pool Chlorine Label</title>
<link href="https://fonts.googleapis.com/css2?family=Montserrat:wght@700;800;900&display=swap" rel="stylesheet">
<style>
  :root {
    --label-bg: #e4e5e7;
    --label-edge: #d2d4d7;
    --brand-red: #b01c1e;
    --navy: #2c5486;
    --navy-deep: #1f3f6e;
    --water-dark: #1d3f7a;
    --water-mid: #2f6fb0;
    --water-light: #4fb6d6;
    --band-text: #ffffff;
    --kg-blue: #6b8fba;
  }
  * { margin: 0; padding: 0; box-sizing: border-box; }
  html, body { width: 1200px; height: 1200px; overflow: hidden; }
  body {
    background: var(--label-bg);
    font-family: "Montserrat", sans-serif;
  }
  .label {
    position: relative;
    width: 1200px;
    height: 1200px;
    background: linear-gradient(90deg, var(--label-edge) 0%, var(--label-bg) 18%, #ececee 50%, var(--label-bg) 82%, var(--label-edge) 100%);
    display: flex;
    flex-direction: column;
    align-items: center;
  }
  .brand {
    margin-top: 150px;
    font-weight: 800;
    font-size: 92px;
    line-height: 1;
    color: var(--brand-red);
    letter-spacing: -1px;
  }
  .water-fill {
    background: linear-gradient(135deg, var(--water-mid) 0%, var(--water-light) 30%, var(--water-dark) 55%, var(--water-mid) 78%, var(--water-light) 100%);
    -webkit-background-clip: text;
    background-clip: text;
    color: transparent;
  }
  .product-name {
    margin-top: 60px;
    padding: 0 24px;
    font-weight: 900;
    font-size: 176px;
    line-height: 0.9;
    letter-spacing: -2px;
  }
  .strength-row {
    position: relative;
    display: flex;
    align-items: flex-end;
  }
  .strength {
    padding: 0 40px 0 22px;
    font-weight: 900;
    font-size: 500px;
    line-height: 0.78;
    letter-spacing: -18px;
    margin-top: 30px;
  }
  .net-weight {
    position: absolute;
    right: -80px;
    bottom: -6px;
    font-weight: 800;
    font-size: 40px;
    color: var(--kg-blue);
  }
  .net-weight small {
    font-size: 22px;
    font-weight: 700;
  }
  .chemical {
    margin-top: 40px;
    font-weight: 800;
    font-size: 40px;
    color: var(--navy);
    letter-spacing: -0.5px;
  }
  .benefits {
    margin-top: 26px;
    display: flex;
    align-items: center;
    gap: 22px;
  }
  .benefit {
    font-weight: 800;
    font-size: 30px;
    line-height: 1.05;
    color: var(--navy);
    text-align: center;
  }
  .divider {
    width: 4px;
    height: 66px;
    background: var(--navy);
  }
  .highlight-band {
    margin-top: 16px;
    width: 790px;
    height: 64px;
    background: linear-gradient(90deg, var(--navy-deep), var(--navy), var(--navy-deep));
    display: flex;
    align-items: center;
    justify-content: center;
    gap: 40px;
    font-weight: 800;
    font-size: 30px;
    color: var(--band-text);
  }
</style>
</head>
<body>
  <main class="label">
    <div class="brand">Valmo</div>
    <div class="product-name water-fill" role="img" aria-label="TORVA lettering filled with clear pool water texture">TORVA</div>
    <div class="strength-row">
      <div class="strength water-fill" role="img" aria-label="60 numerals filled with clear pool water texture">60</div>
      <div class="net-weight">10<small>kg</small></div>
    </div>
    <div class="chemical">TRICHOROISOCYANURIC ACID</div>
    <div class="benefits">
      <div class="benefit">STRONG<br>BLEACHING</div>
      <div class="divider"></div>
      <div class="benefit">DISINFECTION<br>EFFECTS</div>
      <div class="divider"></div>
      <div class="benefit">KILLS BACTERIA<br>AND ALGAE</div>
    </div>
    <div class="highlight-band">
      <span>• LONG-TERM EFFECTS</span>
      <span>• QUALITY GUARANTEE</span>
    </div>
  </main>
</body>
</html>
```